Cool Website Design Bright Coat Studio.

We need a new website, using our existing domain, with a similar function to https://www.plomfilmworks.com/ or https://www.trexafoilcraft.com/ instagram bright_coat.studio.
We can send google docs with pictures.
Logo attached

```html
<!DOCTYPE html>
<html lang="en">
<head>
<meta charset="utf-8">
<title>Bright Coat Studio</title>
<link href="https://fonts.googleapis.com/css2?family=Archivo:wght@400;500;600;700&family=Inter:wght@400;500;600&display=swap" rel="stylesheet">
<style>
:root{
  --bg:#000;
  --navy:#0c0f33;
  --panel:#0b0b0f;
  --line:#2a2a34;
  --purple:#7c3ae6;
  --blue:#1f9cf0;
  --grad:linear-gradient(90deg,var(--purple),var(--blue));
  --text:#fff;
  --muted:#c9c9d4;
  --star:#f6b321;
}
*{margin:0;padding:0;box-sizing:border-box}
html,body{width:1200px;height:4096px;overflow:hidden;background:var(--bg)}
body{position:relative;font-family:"Inter",sans-serif;color:var(--text)}
.abs{position:absolute}
.head{font-family:"Archivo",sans-serif;font-weight:500;text-transform:uppercase;letter-spacing:.2px}
.glow{position:absolute;left:0;top:0;width:1200px;height:1900px;
  background:radial-gradient(ellipse 700px 900px at 120px 700px,rgba(35,40,120,.55),transparent 70%),
             radial-gradient(ellipse 900px 500px at 300px 250px,rgba(25,30,95,.7),transparent 70%),
             radial-gradient(ellipse 500px 700px at 1150px 1500px,rgba(40,30,110,.45),transparent 70%)}
/* nav */
.logo{font-family:"Archivo",sans-serif;font-weight:700;color:#8b5cf6;text-transform:uppercase;line-height:1.05}
.nav a{position:absolute;top:32px;font-family:"Archivo",sans-serif;font-size:10px;font-weight:600;color:#fff;text-decoration:none;letter-spacing:.3px}
.btn{position:absolute;display:flex;align-items:center;justify-content:center;font-family:"Archivo",sans-serif;font-size:10px;font-weight:600;color:#fff;text-transform:uppercase;letter-spacing:.3px;z-index:1}
.btn::before{content:"";position:absolute;inset:0;transform:skewX(-20deg);z-index:-1}
.btn.fill::before{background:var(--grad)}
.btn.line::before{border:1.5px solid var(--blue);border-left-color:var(--purple);border-top-color:#4a6ee8}
/* hero */
.hero-image{left:469px;top:165px;z-index:0}
.hero-title{left:146px;top:208px;font-size:30px;line-height:38px;white-space:nowrap;z-index:2}
.hero-title span{color:#8b5cf6}
.hero-copy{left:146px;top:330px;width:440px;font-size:10px;line-height:15px;color:var(--muted);z-index:2}
/* about */
.about-kicker{left:687px;top:764px;font-size:15px;color:#8b5cf6}
.about-title{left:687px;top:784px;font-size:31px}
.about-copy{left:687px;top:828px;width:340px;font-size:10.5px;line-height:18px;color:var(--muted)}
/* services */
.section-title{left:0;width:1200px;text-align:center;font-size:31px}
.card{position:absolute;width:294px;height:314px}
.card .bgshape{position:absolute;inset:0;background:var(--panel);clip-path:polygon(10% 0,100% 0,90% 100%,0 100%);border:1px solid var(--line)}
.card .photo{position:absolute;left:30px;top:10px;width:254px;height:168px;clip-path:polygon(6% 0,100% 0,100% 100%,0 100%)}
.card h3{position:absolute;left:48px;top:200px;font-size:12.5px}
.card p{position:absolute;left:48px;top:222px;width:200px;font-size:10px;line-height:18px;color:var(--muted)}
.card .btn{left:52px;top:262px;width:162px;height:29px}
/* reviews */
.review{position:absolute;width:238px;height:198px}
.review .bgshape{position:absolute;inset:0;background:var(--panel);border:1px solid #1b1b22;clip-path:polygon(8% 0,100% 0,92% 100%,0 100%)}
.review .avatar{position:absolute;left:55px;top:43px;width:36px;height:36px;border-radius:50%;background:linear-gradient(135deg,#5d6b7a,#b9a58b)}
.review .name{position:absolute;left:100px;top:44px;font-size:11.5px;font-weight:600}
.review .stars{position:absolute;left:100px;top:58px;font-size:12px;color:var(--star);letter-spacing:-.5px}
.review .quote{position:absolute;left:60px;top:94px;width:120px;font-size:10px;line-height:16px;color:var(--muted)}
.review .more{position:absolute;left:60px;top:148px;font-size:10px;color:#8a8a96}
/* contact */
.field{position:absolute;border:1px solid #2c2c33;background:#050507;font-size:10px;padding:14px 18px;color:#d8d8e0}
.footer h4{position:absolute;font-family:"Archivo",sans-serif;font-weight:500;font-size:15px;text-transform:uppercase}
.footer ul{position:absolute;list-style:none;font-size:10.5px;line-height:20px;color:var(--muted)}
.social{position:absolute;top:3907px;width:20px;height:20px;border-radius:50%;border:1px solid #55555f}
</style>
</head>
<body>
<div class="glow"></div>

<!-- Navigation -->
<header>
  <div class="abs logo" style="left:150px;top:12px;font-size:15px;width:120px">Bright Coat<br>Studio</div>
  <nav class="nav">
    <svg class="abs" style="left:511px;top:32px" width="11" height="10" viewBox="0 0 11 10"><path d="M5.5 0L0 5h1.5v5h3V7h2v3h3V5H11z" fill="#3f7bea"/></svg>
    <a style="left:540px">ABOUT US</a>
    <a style="left:609px">SERVICES</a>
    <a style="left:674px">GALLERY</a>
    <a style="left:738px">GET A QUOTE</a>
    <a style="left:818px">REVIEWS</a>
  </nav>
  <div class="btn fill" style="left:880px;top:26px;width:92px;height:26px">Get a Quote</div>
  <svg class="abs" style="left:982px;top:32px" width="10" height="10" viewBox="0 0 24 24"><path d="M6.6 10.8a15 15 0 006.6 6.6l2.2-2.2c.3-.3.7-.4 1-.2 1.1.4 2.3.6 3.6.6.6 0 1 .4 1 1V20c0 .6-.4 1-1 1A17 17 0 013 4c0-.6.4-1 1-1h3.5c.6 0 1 .4 1 1 0 1.3.2 2.5.6 3.6.1.3 0 .7-.2 1z" fill="#3f7bea"/></svg>
  <div class="abs" style="left:995px;top:31px;font-size:10px;font-weight:600;font-family:Archivo,sans-serif">555-014-2290</div>
</header>

<!-- Hero -->
<section class="hero">
  <svg class="abs hero-image" width="731" height="412" viewBox="0 0 731 412" role="img" aria-label="White sports sedan parked on a grassy roadside">
    <defs><linearGradient id="heroPhoto" x1="0" y1="0" x2="1" y2="1"><stop offset="0" stop-color="#6b7560"/><stop offset=".5" stop-color="#a8a69a"/><stop offset="1" stop-color="#3a3d39"/></linearGradient></defs>
    <polygon points="321,0 731,0 731,412 100,412 0,320" fill="url(#heroPhoto)"/>
    <polygon points="330,412 640,0 700,0 390,412" fill="#000"/>
    <polygon points="0,320 150,320 80,412 0,412" fill="#000"/>
  </svg>
  <h1 class="abs head hero-title">Protect your ride or<br>transform your <span>style</span> without<br>breaking the bank</h1>
  <p class="abs hero-copy">Trusted by hundreds of Voltra owners, automotive enthusiasts, and dealerships across Calgary. We provide Lumaguard Paint Protection Film, Vinyl Wraps, Window Tinting, Ceramic Coating, and Coloured PPF from top brands like Northfilm, Kestrel, Orwell Vinyl, and Veltra.</p>
  <div class="btn fill" style="left:152px;top:394px;width:138px;height:29px">Protect my Vehicle</div>
  <div class="btn line" style="left:300px;top:394px;width:140px;height:29px">Change my Colour</div>
</section>

<!-- About -->
<section class="about">
  <div class="abs" style="left:170px;top:604px;width:151px;height:170px;border:1.5px solid #3a3ec8;border-right:none;border-bottom:none"></div>
  <div class="abs" role="img" aria-label="Deep blue sports sedan parked by a stone retaining wall" style="left:195px;top:621px;width:428px;height:412px;background:linear-gradient(160deg,#56704a 0%,#3b4fb0 45%,#1e2a8c 70%,#4f4f4a 100%);clip-path:polygon(0 0,80% 0,100% 20%,100% 100%,20% 100%,0 80%)"></div>
  <div class="abs head about-kicker">About</div>
  <h2 class="abs head about-title">bright_coat.studio</h2>
  <p class="abs about-copy">At bright_coat.studio, we combine passion, precision, and premium products to protect and personalize your vehicle. From Lumaguard Clear PPF to vibrant vinyl wraps, our expert team ensures every project is flawless. Official partners of Voltra Owners Club of Alberta, PrairieVolt, and Ridgeway EV Owners Canada communities.</p>
</section>

<!-- Services -->
<section class="services">
  <h2 class="abs head section-title" style="top:1130px">Our Services</h2>

  <article class="card" style="left:191px;top:1184px"><div class="bgshape"></div>
    <div class="photo" role="img" aria-label="Installer applying paint protection film to a black car" style="background:linear-gradient(135deg,#7a1420,#1a1a1e 55%,#9a9aa0)"></div>
    <h3 class="head">Paint Protection Film (PPF)</h3><p>Protects paint; clear, matte, stealth &amp; coloured options.</p><div class="btn line">Learn More</div></article>
  <article class="card" style="left:453px;top:1184px"><div class="bgshape"></div>
    <div class="photo" role="img" aria-label="Hands stretching glossy blue vinyl wrap" style="background:linear-gradient(135deg,#1e3fa8,#3b7ee8 50%,#cfd3dc)"></div>
    <h3 class="head">Vinyl Wraps</h3><p>Customize your car with hundreds of colours &amp; finishes.</p><div class="btn line">Learn More</div></article>
  <article class="card" style="left:715px;top:1184px"><div class="bgshape"></div>
    <div class="photo" role="img" aria-label="Hands smoothing window tint film on glass" style="background:linear-gradient(135deg,#2a2a2e,#8a8c90 50%,#1c1c20)"></div>
    <h3 class="head">Window Tinting</h3><p>UV protection with stylish light &amp; dark tints.</p><div class="btn line">Learn More</div></article>

  <article class="card" style="left:191px;top:1514px"><div class="bgshape"></div>
    <div class="photo" role="img" aria-label="Hatchback wrapped in colour-shift purple and gold film" style="background:linear-gradient(135deg,#6a6e5a,#6b3fa0 45%,#c9a04a 75%,#5a5a58)"></div>
    <h3 class="head">Coloured PPF</h3><p>Add colour to select vehicles, including Voltra Ridgeline.</p><div class="btn line">Learn More</div></article>
  <article class="card" style="left:453px;top:1514px"><div class="bgshape"></div>
    <div class="photo" role="img" aria-label="Detailer polishing a grey car fender" style="background:linear-gradient(135deg,#d8d8dc,#6a6c72 50%,#2a2b30)"></div>
    <h3 class="head">Pro Detailing</h3><p>Interior &amp; exterior cleaning, polishing, and paint correction.</p><div class="btn line">Learn More</div></article>
  <article class="card" style="left:715px;top:1514px"><div class="bgshape"></div>
    <div class="photo" role="img" aria-label="Ceramic coating being applied to a blue car bonnet" style="background:linear-gradient(135deg,#cfd4de,#1f3f9a 55%,#0e1a4a)"></div>
    <h3 class="head">Ceramic Coating</h3><p>Hydrophobic coating for easier maintenance and long-lasting shine.</p><div class="btn line">Learn More</div></article>

  <div class="btn fill" style="left:507px;top:1867px;width:186px;height:29px">Learn more about services</div>
</section>

<!-- Gallery -->
<section class="gallery">
  <h2 class="abs head section-title" style="top:1978px">Our Work Speaks For Itself</h2>
  <p class="abs" style="left:0;width:1200px;top:2024px;text-align:center;font-size:10.5px;color:var(--muted)">See some of our latest vinyl wraps, PPF, and custom detailing projects.</p>
  <svg class="abs" style="left:0;top:2080px" width="1200" height="265" viewBox="0 0 1200 265" role="img" aria-label="Gallery of wrapped and protected vehicles">
    <defs>
      <linearGradient id="g1" x1="0" y1="0" x2="0" y2="1"><stop offset="0" stop-color="#8a9aa8"/><stop offset="1" stop-color="#1c2230"/></linearGradient>
      <linearGradient id="g2" x1="0" y1="0" x2="1" y2="1"><stop offset="0" stop-color="#3a3a3e"/><stop offset=".6" stop-color="#c8202c"/><stop offset="1" stop-color="#6a6a6e"/></linearGradient>
      <linearGradient id="g3" x1="0" y1="0" x2="1" y2="1"><stop offset="0" stop-color="#1f7fe6"/><stop offset="1" stop-color="#7b3ae6"/></linearGradient>
      <linearGradient id="g4" x1="0" y1="0" x2="0" y2="1"><stop offset="0" stop-color="#9aa0a8"/><stop offset=".6" stop-color="#b0a8a0"/><stop offset="1" stop-color="#4a4a48"/></linearGradient>
      <linearGradient id="g5" x1="0" y1="0" x2="1" y2="1"><stop offset="0" stop-color="#8a8a8e"/><stop offset=".5" stop-color="#c4202a"/><stop offset="1" stop-color="#6a6a6a"/></linearGradient>
      <linearGradient id="g6" x1="0" y1="0" x2="1" y2="1"><stop offset="0" stop-color="#b6bcc2"/><stop offset="1" stop-color="#3a3c40"/></linearGradient>
    </defs>
    <polygon points="0,0 172,0 142,265 0,265" fill="url(#g1)"/>
    <polygon points="179,0 394,0 364,265 149,265" fill="url(#g2)"/>
    <polygon points="401,0 617,0 587,265 371,265" fill="url(#g3)"/>
    <polygon points="624,0 834,0 804,265 594,265" fill="url(#g4)"/>
    <polygon points="841,0 1054,0 1024,265 811,265" fill="url(#g5)"/>
    <polygon points="1061,0 1200,0 1200,265 1031,265" fill="url(#g6)"/>
    <rect x="463" y="121" width="22" height="22" fill="#fff"/>
    <circle cx="473" cy="131" r="4" fill="none" stroke="#222" stroke-width="1.5"/><line x1="476" y1="134" x2="479" y2="137" stroke="#222" stroke-width="1.5"/>
    <rect x="492" y="121" width="22" height="22" fill="#fff"/>
    <line x1="498" y1="137" x2="508" y2="127" stroke="#222" stroke-width="2"/>
  </svg>
  <div class="btn line" style="left:482px;top:2380px;width:236px;height:29px">See more wrapped and PPF vehicles</div>
</section>

<!-- Reviews -->
<section class="reviews">
  <h2 class="abs head section-title" style="top:2496px">What Our Customers Say</h2>
  <div class="abs" style="left:949px;top:2508px;font-family:Archivo,sans-serif;font-size:9.5px;font-weight:600;padding-bottom:4px;border-bottom:2px solid var(--blue)">READ MORE REVIEWS</div>
  <div class="abs" style="left:0;width:1200px;top:2538px;text-align:center;font-size:10px">4.9<span style="color:var(--star)">★</span> (138 Reviews)</div>

  <article class="review" style="left:156px;top:2577px"><div class="bgshape"></div><div class="avatar" role="img" aria-label="Reviewer avatar"></div>
    <div class="name">Marcus T</div><div class="stars">★★★★★</div><p class="quote">My Voltra looks better than showroom fresh. Amazing team!</p><div class="more">Read More</div></article>
  <article class="review" style="left:374px;top:2577px"><div class="bgshape"></div><div class="avatar" role="img" aria-label="Reviewer avatar"></div>
    <div class="name">Devon R.</div><div class="stars">★★★★★</div><p class="quote">Super transparent and humble guys. Process was easy and smooth.</p><div class="more">Read More</div></article>
  <article class="review" style="left:592px;top:2577px"><div class="bgshape"></div><div class="avatar" role="img" aria-label="Reviewer avatar"></div>
    <div class="name">Priya S</div><div class="stars">★★★★★</div><p class="quote">The price is right and service is top-notch. Highly recommend!</p><div class="more">Read More</div></article>
  <article class="review" style="left:810px;top:2577px"><div class="bgshape"></div><div class="avatar" role="img" aria-label="Reviewer avatar"></div>
    <div class="name">Marcus T</div><div class="stars">★★★★★</div><p class="quote">My Voltra looks better than showroom fresh. Amazing team!</p><div class="more">Read More</div></article>
</section>

<!-- Financing -->
<section class="financing">
  <div class="abs" style="left:146px;top:2849px;width:906px;height:143px;background:linear-gradient(90deg,#6b2fd8,#4a5fe6 45%,#1a9af0);clip-path:polygon(10% 0,100% 0,90% 100%,0 100%)"></div>
  <h2 class="abs head" style="left:256px;top:2893px;font-size:25px">Flexible Options For Everyone</h2>
  <p class="abs" style="left:256px;top:2924px;width:360px;font-size:10px;line-height:18px;color:#e8e8f4">No Interest. No Payments for 3 Months. Apply for financing today and make your dream wrap affordable.</p>
  <div class="btn" style="left:830px;top:2906px;width:140px;height:29px;color:#111;text-transform:none"><span style="position:absolute;inset:0;background:#fff;transform:skewX(-20deg);z-index:-1"></span>APPLY FOR FINANCING</div>
</section>

<!-- Contact -->
<section class="contact">
  <h2 class="abs head" style="left:278px;top:3124px;font-size:31px">Contact Us</h2>
  <div class="field" style="left:148px;top:3176px;width:221px;height:43px">Name*</div>
  <div class="field" style="left:375px;top:3176px;width:221px;height:43px">Phone*</div>
  <div class="field" style="left:148px;top:3227px;width:448px;height:42px">Email*</div>
  <div class="field" style="left:148px;top:3280px;width:448px;height:124px;padding-top:18px">Message</div>
  <div class="btn fill" style="left:328px;top:3413px;width:92px;height:29px">Submit Now</div>

  <div class="abs" style="left:629px;top:3067px;width:142px;height:159px;border:1.5px solid #3a3ec8;border-right:none;border-bottom:none"></div>
  <div class="abs" role="img" aria-label="Map showing the studio location" style="left:652px;top:3086px;width:400px;height:384px;background:linear-gradient(135deg,#e6e6e6,#d6d6d6);clip-path:polygon(0 0,80% 0,100% 20%,100% 100%,20% 100%,0 80%)"></div>
  <svg class="abs" style="left:856px;top:3240px" width="24" height="34" viewBox="0 0 24 34"><path d="M12 0C5.4 0 0 5.4 0 12c0 9 12 22 12 22s12-13 12-22C24 5.4 18.6 0 12 0z" fill="#3f6bea"/><circle cx="12" cy="12" r="4.5" fill="#fff"/></svg>
</section>

<!-- Call to action -->
<section class="cta">
  <div class="abs" style="left:0;top:3559px;width:1200px;height:160px;background:#101012;clip-path:polygon(6% 0,94% 0,100% 100%,0 100%)"></div>
  <h2 class="abs head" style="left:146px;top:3620px;font-size:30px">Protect your paint. Look good doing it.</h2>
  <div class="btn fill" style="left:904px;top:3625px;width:100px;height:30px">Wrap my car</div>
  <div class="abs" style="left:146px;top:3710px;width:906px;height:1px;background:#2a2a30"></div>
</section>

<!-- Footer -->
<footer class="footer">
  <div class="abs logo" style="left:152px;top:3838px;font-size:25px;width:200px">Bright Coat<br>Studio</div>

  <h4 style="left:442px;top:3806px">Useful Links</h4>
  <ul style="left:442px;top:3835px"><li>Home</li><li>About</li><li>Services</li><li>Gallery</li><li>Reviews</li><li>Contact</li></ul>

  <h4 style="left:640px;top:3806px">Top Services</h4>
  <ul style="left:640px;top:3835px"><li>Vinyl Wraps</li><li>Lumaguard Paint Protection Film</li><li>Matte Paint Protection Film</li><li>Coloured PPF</li><li>Ceramic Coating</li><li>Car Detailing</li><li>Custom Decals</li></ul>

  <h4 style="left:855px;top:3806px">Contact Us</h4>
  <ul style="left:872px;top:3835px"><li>555-014-2290</li><li>240 Harlow Street NE, Calgary, AB</li><li>hello@brightcoat.studio</li></ul>
  <svg class="abs" style="left:855px;top:3841px" width="9" height="9" viewBox="0 0 24 24"><path d="M6.6 10.8a15 15 0 006.6 6.6l2.2-2.2c.3-.3.7-.4 1-.2 1.1.4 2.3.6 3.6.6.6 0 1 .4 1 1V20c0 .6-.4 1-1 1A17 17 0 013 4c0-.6.4-1 1-1h3.5c.6 0 1 .4 1 1 0 1.3.2 2.5.6 3.6.1.3 0 .7-.2 1z" fill="#6a7cf0"/></svg>
  <svg class="abs" style="left:856px;top:3860px" width="8" height="11" viewBox="0 0 24 34"><path d="M12 0C5.4 0 0 5.4 0 12c0 9 12 22 12 22s12-13 12-22C24 5.4 18.6 0 12 0z" fill="#6a7cf0"/></svg>
  <svg class="abs" style="left:855px;top:3882px" width="10" height="8" viewBox="0 0 20 16"><rect width="20" height="16" rx="2" fill="#6a7cf0"/><path d="M1 2l9 7 9-7" stroke="#000" stroke-width="1.5" fill="none"/></svg>
  <span class="social" style="left:855px"></span><span class="social" style="left:882px"></span><span class="social" style="left:909px"></span><span class="social" style="left:936px"></span>

  <p class="abs" style="left:0;width:1200px;top:4027px;text-align:center;font-size:10.5px;line-height:20px;color:var(--muted)">© 2025 bright_coat.studio. All rights reserved. Official Alberta Voltra<br>Partners. ADLC Licensed.</p>

  <div class="abs" style="left:1076px;top:3938px;width:64px;height:64px;border-radius:50%;background:#2f56d8"></div>
  <svg class="abs" style="left:1094px;top:3956px" width="28" height="28" viewBox="0 0 28 28"><path d="M14 3C7.4 3 3 7.4 3 12.5c0 3 1.5 5.6 4 7.3V25l4.6-3c.8.2 1.6.3 2.4.3 6.6 0 11-4.4 11-9.8S20.6 3 14 3z" fill="#0b0b14"/></svg>
</footer>
</body>
</html>
```